Flyer Design Project

I am opening a yoga studio called Willowmere Yoga .Pilates. Fitness
and require a flyer that will be letterbox dropped. It will two sided - DL size.100mm × 210mm

The studio will offer Vinyasa Flow Yoga and Mat Pilates classes. We aim to enable people to lead healthier, happier lives through improved strength, flexibility and general well being that regular yoga and pilates practice offers.

We offer group classes, private and semi private sessions in yoga and pilates.

it must have the logo on it- I have uploaded the logo in two versions - not sure what will look the best.

pick up one of the colours from the logo as the background colour.

Side one:
Simple and clean with one side showing logo and address details, website and with simple intro about studio (if it fits)

Location: 1st Floor, 17 Larkspur Parade, Tindale, 3286
phone: 0428 596143
www.willowmeretindale.com.au

OPENING OCTOBER

other side - class descriptions and intro offer for new clients
$20 for 7 days of classes
$99 for 1 month unlimited.

Class descriptions:
Vinyasa Flow yoga: A class that flows from pose to pose integrating breath, alignment, strength and power. All levels are catered for in a warm room heated to around 26 degrees. You will leave feeling inspired, empowered and energised.

Mat Pilates: A strong, challenging class integrating the key principles of pilates: concentration, control, centring, precision, flowing movement and breath. Using the core as a focus to develop these principles you will be hooked on the physical freedom you experience post workout:improved strength, flexibility and vitality that pilates offers.

Private and semi Private tuition available.

Target Market(s)

mainly women, athletic, 35-55 age, middle class, well educated

Industry/Entity Type

Fitness

Requirements
Must have
• 2 pages
the logo

Should not have
• no pics

```html
<!DOCTYPE html>
<html lang="en">
<head>
<meta charset="utf-8">
<title>Willowmere Yoga – DL Flyer</title>
<link href="https://fonts.googleapis.com/css2?family=Open+Sans:wght@400;600;700&family=Barlow+Condensed:ital,wght@1,600;1,700&family=Marck+Script&display=swap" rel="stylesheet">
<style>
  :root{
    --stage:#eceee6;
    --paper:#ffffff;
    --teal:#2a9ba6;
    --aqua:#4cc6e0;
    --red:#e8322b;
    --orange:#f39a3c;
    --peach:#f6c58f;
    --peach-soft:#fbe3c8;
    --ink:#3c3c3c;
    --grey:#8a8f95;
    --shadow:rgba(0,0,0,.18);
  }
  *{box-sizing:border-box;margin:0;padding:0}
  html,body{width:927px;height:1200px;overflow:hidden}
  body{background:var(--stage);font-family:"Open Sans",Arial,sans-serif;position:relative}

  .flyer{position:absolute;top:170px;width:410px;height:861px;background:var(--paper);
    box-shadow:0 4px 14px var(--shadow);overflow:hidden}
  .flyer--front{left:36px}
  .flyer--back{left:481px}

  .top-band{position:absolute;top:0;left:0;right:0;height:14px;
    background:linear-gradient(90deg,var(--aqua),var(--red))}
  .artwork-area{position:absolute;left:0;right:0;top:480px;bottom:0;
    background:linear-gradient(180deg,rgba(251,227,200,0) 0%,var(--peach-soft) 45%,var(--peach-soft) 100%)}

  .flyer__content{position:relative;padding:0 26px}

  .brand-head{display:flex;align-items:center;gap:10px;padding-top:50px}
  .brand-head__dot{width:26px;height:26px;border-radius:50%;background:var(--orange);flex:none}
  .brand-head__name{font-weight:600;font-size:19px;color:var(--grey);line-height:1.15}

  .intro{margin-top:22px;font-size:14.2px;line-height:1.42;color:var(--teal);text-align:justify;text-indent:28px}
  .offer-line{margin-top:16px;font-family:"Barlow Condensed",sans-serif;font-style:italic;font-weight:700;
    font-size:17px;color:var(--ink);text-align:center;line-height:1.2;text-transform:uppercase}
  .opening{margin-top:12px;text-align:center;font-family:"Barlow Condensed",sans-serif;font-style:italic;font-weight:700;
    font-size:31px;color:var(--aqua);line-height:1}
  .opening__sub{display:block;font-size:13px;color:var(--ink);font-weight:600;margin-top:2px}
  .prices{margin-top:8px;text-align:center;font-family:"Barlow Condensed",sans-serif;font-style:italic;font-weight:700;
    font-size:24px;color:var(--red);line-height:1.15;text-transform:uppercase}

  .classes-band{margin:22px -26px 0;padding:6px 26px;font-size:15px;font-weight:400;color:var(--ink);
    background:linear-gradient(90deg,var(--peach),rgba(255,255,255,0) 80%)}
  .class{margin-top:8px}
  .class__title{font-family:"Marck Script",cursive;font-size:23px;font-weight:400;color:var(--red);line-height:1.1}
  .class__text{font-size:14px;line-height:1.42;color:var(--ink);text-align:justify;text-indent:28px}
  .tuition{margin-top:16px;font-size:13.5px;color:var(--ink)}

  .brand-foot{position:absolute;right:22px;bottom:44px;display:flex;align-items:center;gap:8px}
  .brand-foot__dot{width:22px;height:22px;border-radius:50%;background:var(--orange)}
  .brand-foot__name{font-weight:700;font-size:13px;color:var(--ink);text-align:right;line-height:1.2}
  .web-strip{position:absolute;right:0;bottom:12px;width:200px;padding:4px 14px;background:var(--red);
    color:#fff;font-size:11px;font-weight:600;text-align:right}

  .back-block{position:absolute;top:330px;left:0;right:0;display:flex;flex-direction:column;align-items:center}
  .back-block__dot{width:70px;height:70px;border-radius:50%;background:var(--orange)}
  .back-block__name{margin-top:10px;font-weight:700;font-size:15px;color:var(--ink);text-align:center;line-height:1.25}
  .contact{margin-top:10px;font-size:11.5px;font-weight:600;color:var(--ink);text-align:center;line-height:1.45;max-width:210px}
</style>
</head>
<body>

<section class="flyer flyer--front">
  <div class="top-band"></div>
  <div class="artwork-area" role="img" aria-label="Decorative sunburst glow and curved swoosh artwork"></div>
  <div class="flyer__content">
    <header class="brand-head">
      <span class="brand-head__dot"></span>
      <span class="brand-head__name">Willowmere Yoga .Pilates. Fitness</span>
    </header>
    <p class="intro">The studio will offer Vinyasa Flow Yoga and Mat Pilates classes. We aim to enable people to lead healthier, happier lives through improved strength, flexibility and general well being that regular yoga and pilates practice offers.</p>
    <p class="offer-line">We offer group classes, private and semi private sessions in yoga and pilates.</p>
    <p class="opening">OPENING OCTOBER<span class="opening__sub">CLASS DESCRIPTIONS AND INTRO OFFER FOR NEW CLIENTS</span></p>
    <p class="prices">$20 for 7 days of classes<br>$99 for 1 month unlimited.</p>
    <h2 class="classes-band">Class descriptions:</h2>
    <div class="class">
      <h3 class="class__title">Vinyasa Flow yoga:</h3>
      <p class="class__text">A class that flows from pose to pose integrating breath, alignment, strength and power. All levels are catered for in a warm room heated to around 26 degrees. You will leave feeling inspired, empowered and energised.</p>
    </div>
    <div class="class">
      <h3 class="class__title">Mat Pilates:</h3>
      <p class="class__text">A strong, challenging class integrating the key principles of pilates: concentration, control, centring, precision, flowing movement and breath. Using the core as a focus to develop these principles you will be hooked on the physical freedom you experience post workout: improved strength, flexibility and vitality that pilates offers.</p>
    </div>
    <p class="tuition">Private and semi Private tuition available.</p>
  </div>
  <div class="brand-foot">
    <span class="brand-foot__dot"></span>
    <span class="brand-foot__name">Willowmere Yoga<br>.Pilates. Fitness</span>
  </div>
  <div class="web-strip">www.willowmeretindale.com.au</div>
</section>

<section class="flyer flyer--back">
  <div class="back-block">
    <span class="back-block__dot"></span>
    <p class="back-block__name">Willowmere Yoga<br>.Pilates. Fitness</p>
    <p class="contact">Location: 1st Floor, 17 Larkspur Parade, Tindale, 3286<br>phone: 0428 596143<br>www.willowmeretindale.com.au</p>
  </div>
</section>

</body>
</html>
```